Design for a 4 screens mobile app: Brightnook

The app is a compact but illustrated phone/address book...
We need a design for the 5 screens of the app (see screens attached):
a) "index" : 1 screen with 6 pictures of contact person
b) "contact list" : 1 screen, to manage (add/del/edit) the contacts of the phone/address book
c) "add contact" : 1 screen to add a contact (a picture + a phone number)
d) "update contact" : similar to "add"
e) "fields missing" : add/edit screens in "error" state
We also need the ico design + loading screen.
No specific guidelines, nor logo or whatever.
It will be a free app distributed on iOS and Androïd.
We just want to make it looking nice & very usable for end users.
B2C

```html
<!DOCTYPE html>
<html lang="en">
<head>
<meta charset="utf-8">
<title>Brightnook – Update Contact Screen</title>
<link href="https://fonts.googleapis.com/css2?family=Lato:wght@300;400;700&display=swap" rel="stylesheet">
<style>
  :root {
    --coral: #f37474;
    --coral-deep: #f06a6b;
    --screen-bg: #f0f0f0;
    --white: #ffffff;
    --green: #62bb46;
    --photo-dark: #2b2424;
    --photo-mid: #8a7d74;
    --photo-light: #d9d2c8;
  }
  * { margin: 0; padding: 0; box-sizing: border-box; }
  html, body {
    width: 1200px;
    height: 675px;
    overflow: hidden;
    background: var(--coral);
    font-family: "Lato", sans-serif;
  }
  .stage {
    position: relative;
    width: 1200px;
    height: 675px;
    background: var(--coral);
  }
  .app-screen {
    position: absolute;
    left: 133px;
    top: 175px;
    width: 279px;
    height: 500px;
    background: var(--screen-bg);
    overflow: hidden;
  }
  .status-bar {
    height: 15px;
    background: var(--coral);
    color: var(--white);
    font-size: 7.5px;
    font-weight: 700;
    display: flex;
    align-items: center;
    justify-content: space-between;
    padding: 0 6px;
    position: relative;
  }
  .status-left, .status-right { display: flex; align-items: center; gap: 4px; }
  .status-time {
    position: absolute;
    left: 50%;
    transform: translateX(-50%);
  }
  .nav-bar {
    height: 37px;
    background: var(--coral);
    color: var(--white);
    display: flex;
    align-items: center;
    justify-content: space-between;
    padding: 0 12px;
  }
  .nav-title { font-size: 12px; font-weight: 400; }
  .contact-photo {
    width: 279px;
    height: 279px;
    background: linear-gradient(135deg, var(--photo-light) 0%, var(--photo-mid) 45%, var(--photo-dark) 100%);
  }
  .phone-number {
    position: absolute;
    left: 66px;
    top: 367px;
    width: 145px;
    height: 33px;
    background: var(--coral-deep);
    color: var(--white);
    border-radius: 2px;
    font-size: 13.5px;
    display: flex;
    align-items: center;
    justify-content: center;
  }
  .action-icon { position: absolute; top: 420px; }
  .action-delete { left: 66px; }
  .action-gallery { left: 175px; }
  .screen-caption {
    position: absolute;
    left: 487px;
    top: 354px;
    color: var(--white);
    font-weight: 300;
    font-size: 35px;
    letter-spacing: 0.3px;
  }
</style>
</head>
<body>
<main class="stage">
  <section class="app-screen">
    <div class="status-bar">
      <div class="status-left">
        <svg width="12" height="5" viewBox="0 0 12 5" fill="#fff"><rect x="0" y="3" width="1.6" height="2"/><rect x="2.5" y="2.2" width="1.6" height="2.8"/><rect x="5" y="1.5" width="1.6" height="3.5"/><rect x="7.5" y="0.7" width="1.6" height="4.3"/><rect x="10" y="0" width="1.6" height="5"/></svg>
        <span>NT CZ</span>
        <svg width="9" height="7" viewBox="0 0 9 7" fill="none" stroke="#fff" stroke-width="1.1"><path d="M0.8 2.6a5.3 5.3 0 0 1 7.4 0"/><path d="M2.2 4a3.2 3.2 0 0 1 4.6 0"/><circle cx="4.5" cy="5.8" r="0.6" fill="#fff"/></svg>
      </div>
      <span class="status-time">2:52 PM</span>
      <div class="status-right">
        <svg width="8" height="8" viewBox="0 0 8 8" fill="none" stroke="#fff" stroke-width="1"><circle cx="4" cy="4" r="3.4"/><rect x="2.6" y="3.6" width="2.8" height="2" fill="#fff" stroke="none"/></svg>
        <span>53 %</span>
        <svg width="14" height="7" viewBox="0 0 14 7" fill="none" stroke="#fff" stroke-width="0.8"><rect x="0.5" y="0.5" width="11.5" height="6" rx="1"/><rect x="1.5" y="1.5" width="5.5" height="4" fill="#fff" stroke="none"/><rect x="12.5" y="2.3" width="1" height="2.4" fill="#fff" stroke="none"/></svg>
      </div>
    </div>
    <header class="nav-bar">
      <svg class="nav-back" width="14" height="13" viewBox="0 0 14 13" fill="none" stroke="#fff" stroke-width="2" stroke-linecap="round" stroke-linejoin="round"><path d="M5 1.5 1.5 5 5 8.5"/><path d="M1.5 5h6a4 4 0 0 1 4 4v3"/></svg>
      <span class="nav-title">Update Contact</span>
      <svg class="nav-confirm" width="14" height="14" viewBox="0 0 14 14"><circle cx="7" cy="7" r="7" fill="#fff"/><path d="M3.8 7.2 6 9.3 10.2 4.9" fill="none" stroke="#f37474" stroke-width="1.8" stroke-linecap="round" stroke-linejoin="round"/></svg>
    </header>
    <div class="contact-photo" role="img" aria-label="Contact portrait photo"></div>
    <div class="phone-number">(1) 55 0123 4567</div>
    <svg class="action-icon action-delete" width="34" height="34" viewBox="0 0 34 34" aria-label="Delete photo">
      <path d="M4 9 Q10 1 18 6" fill="none" stroke="#f06a6b" stroke-width="2.4" stroke-linecap="round"/>
      <path d="M15 3 19 6.5 14.5 8.5Z" fill="#f06a6b"/>
      <path d="M22 3 31 10 M28 2 24 12" stroke="#f06a6b" stroke-width="2.2" stroke-linecap="round"/>
      <rect x="5" y="12" width="20" height="3" rx="1" fill="#f06a6b"/>
      <path d="M7 16h16l-1.6 16H8.6Z" fill="#f06a6b"/>
      <path d="M11.5 19v10M15 19v10M18.5 19v10" stroke="#f0f0f0" stroke-width="1.6" stroke-linecap="round"/>
    </svg>
    <svg class="action-icon action-gallery" width="38" height="36" viewBox="0 0 38 36" aria-label="Choose from gallery">
      <rect x="8" y="10" width="24" height="22" rx="1" fill="var(--green)" transform="rotate(8 20 21)"/>
      <rect x="5" y="7" width="24" height="22" rx="1" fill="#7cc95e" stroke="#f0f0f0" stroke-width="1.2" transform="rotate(4 17 18)"/>
      <rect x="2" y="3" width="24" height="22" rx="1" fill="var(--green)" stroke="#f0f0f0" stroke-width="1.2"/>
      <rect x="5" y="6" width="18" height="16" fill="#f0f0f0"/>
      <circle cx="14" cy="11.5" r="3" fill="var(--green)"/>
      <path d="M8 21a6 5 0 0 1 12 0Z" fill="var(--green)"/>
    </svg>
  </section>
  <h1 class="screen-caption">Update Contact Screen</h1>
</main>
</body>
</html>
```